Website redesign for a technology and engineering company

We'd like to redesign our website which can be found on brovalux.co.nz
!! Please find the designers brief as an uploaded file with all details in there!!
The main purpose for redesign is:
>change of services offered
>old website not very user friendly to maintain or update
Key requirements:
>visually appealing
>easy to navigate
>simple and easy to read
>responsive
>mobile device compatibility
>integrating best SEO practice
All the details are in the attached designer brief document.

Coding
Coded - Design and coding required
Number of Pages Required
1 page
Look and feel
Each slider illustrates characteristics of the customer's brand and the style your logo design should communicate.

```html
<!DOCTYPE html>
<html lang="en">
<head>
<meta charset="utf-8">
<title>Brovalux — Precision. Efficiency. Clarity.</title>
<link href="https://fonts.googleapis.com/css2?family=Outfit:wght@400;500;600;700&display=swap" rel="stylesheet">
<style>
:root{
  --blue:#4a74f5;
  --navy:#0c1330;
  --ink:#111318;
  --text:#2a2d36;
  --muted:#8a8fa0;
  --pale:#f1f5ff;
  --white:#ffffff;
  --line:#9aa0ad;
}
*{box-sizing:border-box;margin:0;padding:0}
html,body{width:1200px;height:4093px;overflow:hidden}
body{position:relative;font-family:"Outfit",sans-serif;color:var(--text);background:var(--white)}
.abs{position:absolute}
svg.band{position:absolute;left:0;display:block}

/* hero */
.hero-photo{left:0;top:0;width:1200px;height:644px;background:linear-gradient(120deg,#1c2536 0%,#2a3a3a 40%,#3c4a3e 70%,#1e2838 100%)}
.hero-photo::after{content:"";position:absolute;inset:0;background:rgba(12,19,48,.45)}
.brand{font-weight:600;color:var(--white);font-size:40px;letter-spacing:.5px;line-height:1}
.brand-dot{display:inline-block;width:14px;height:14px;border-radius:50%;background:var(--white);margin-right:10px;vertical-align:middle}
.btn-outline{border:2px solid var(--white);color:var(--white);border-radius:6px;font-size:13px;font-weight:600;display:flex;align-items:center;justify-content:center;gap:8px}
.hero-title{left:141px;top:218px;font-size:43px;font-weight:700;color:var(--white);letter-spacing:-.3px}
.hero-sub{left:141px;top:284px;width:520px;font-size:14.5px;line-height:26px;color:var(--white)}
.btn-blue{background:var(--blue);color:var(--white);border-radius:6px;font-weight:600;font-size:14px;display:flex;align-items:center;justify-content:center;gap:10px}
.scroll-line{left:994px;top:334px;width:2px;height:112px;background:var(--white)}
.scroll-label{left:972px;top:472px;color:var(--white);font-size:17px;font-weight:600}

/* headings */
.section-title{left:0;width:1200px;text-align:center;font-size:35px;font-weight:700;color:var(--ink)}
.divider{display:flex;align-items:center;gap:8px}
.divider span{display:block;width:26px;height:2px;background:var(--ink)}
.divider i{display:block;width:10px;height:10px;border:2px solid var(--ink);border-radius:50%}

/* about */
.about-photo{left:143px;top:732px;width:452px;height:452px;border-radius:50%;background:linear-gradient(180deg,#9aa3ab 0%,#c4c8cb 45%,#6f8d3d 58%,#4f7a2a 100%)}
.badge{left:144px;top:727px;width:144px;height:144px;border-radius:50%;background:var(--navy);border:9px solid var(--white);color:var(--white);text-align:center;display:flex;flex-direction:column;justify-content:center}
.badge b{font-size:28px;font-weight:700;line-height:1}
.badge small{font-size:10.5px;line-height:14px;margin-top:4px}
.about-title{left:674px;top:800px;font-size:29px;font-weight:700;color:var(--ink)}
.about-text{left:672px;top:872px;width:386px;font-size:13px;line-height:25.4px;color:var(--text);word-break:break-all}
.btn-dark{border:2px solid var(--ink);color:var(--ink);border-radius:7px;font-size:13px;font-weight:600;display:flex;align-items:center;justify-content:center;gap:8px}

/* services */
.services-bg{left:0;top:1271px;width:1200px;height:1050px;background:var(--pale)}
.card{background:var(--white);border-radius:16px;overflow:hidden;box-shadow:0 4px 18px rgba(40,60,120,.06)}
.card-img{height:224px}
.card h3{font-size:20px;font-weight:600;color:var(--ink);margin:28px 0 0 28px}
.card ul{list-style:none;margin:12px 0 0 28px}
.card li{font-size:12px;line-height:34.4px;color:var(--ink);position:relative;padding-left:21px}
.card li::before{content:"";position:absolute;left:0;top:15px;width:5px;height:5px;border-radius:50%;background:var(--ink)}

/* case studies */
.case-img{border-radius:22px}
.case-box{background:var(--white);border-radius:20px;box-shadow:0 6px 26px rgba(20,30,60,.1);padding:30px 30px}
.case-box h4{font-size:18.5px;font-weight:600;color:var(--ink);line-height:25px}
.case-box p{margin-top:20px;font-size:10.5px;line-height:20px;color:var(--text);word-break:break-all}
.nav-arrow{width:30px;height:56px}

/* form */
.field{left:194px;width:812px;border:1.5px solid #a7acb8;border-radius:28px;font-size:12px;color:var(--text);padding-left:35px;display:flex;align-items:center}
.field.active{border-color:var(--blue);color:var(--muted)}
.field.area{border-radius:26px;align-items:flex-start;padding-top:22px}
.float-label{left:232px;top:3097px;background:var(--blue);color:var(--white);font-size:9px;border-radius:10px;padding:4px 18px}

/* footer */
.footer-bg{left:0;top:3650px;width:1200px;height:400px;background:linear-gradient(180deg,#121a33 0%,#0c1330 100%)}
.foot-h{font-size:16px;font-weight:600;color:var(--white);letter-spacing:.3px}
.foot-link{font-size:12.5px;color:var(--white);line-height:25px}
.newsletter{left:828px;top:3853px;width:230px;height:40px;background:var(--white);border-radius:22px;font-size:11.5px;color:#555;display:flex;align-items:center;padding-left:14px}
.nl-btn{position:absolute;right:4px;top:4px;width:32px;height:32px;border-radius:50%;background:var(--blue);display:flex;align-items:center;justify-content:center}
.copyright{left:0;top:4047px;width:1200px;height:46px;background:var(--blue);color:var(--white);font-size:12.5px;display:flex;align-items:center;justify-content:center}
</style>
</head>
<body>

<!-- Hero -->
<div class="abs hero-photo" role="img" aria-label="Technician setting up a GNSS survey station beside a wooden fence and road"></div>
<svg class="band" style="top:500px" width="1200" height="160" viewBox="0 0 1200 160">
  <polygon points="0,24 842,144 1200,32 1200,160 0,160" fill="#ffffff"/>
  <polygon points="0,24 842,144 1200,32 1200,56 842,144 0,58" fill="#4a74f5"/>
</svg>
<div class="abs brand" style="left:143px;top:66px"><span class="brand-dot"></span>Brovalux</div>
<div class="abs btn-outline" style="left:916px;top:46px;width:139px;height:41px">Get in touch
  <svg width="12" height="12" viewBox="0 0 12 12"><path d="M2 10L10 2M4 2h6v6" stroke="#fff" stroke-width="1.6" fill="none"/></svg></div>
<h1 class="abs hero-title">Precision.Efficiency.Clarity.</h1>
<p class="abs hero-sub">Providing precise and reliable technical fieldwork solutions to meet your project needs.</p>
<div class="abs btn-blue" style="left:140px;top:360px;width:154px;height:45px">Contact Us
  <svg width="14" height="14" viewBox="0 0 12 12"><path d="M2 10L10 2M4 2h6v6" stroke="#fff" stroke-width="1.6" fill="none"/></svg></div>
<div class="abs scroll-line"></div>
<svg class="abs" style="left:987px;top:442px" width="16" height="12" viewBox="0 0 16 12"><polygon points="0,0 16,0 8,11" fill="#fff"/></svg>
<div class="abs scroll-label">Scroll</div>

<!-- About -->
<div class="abs about-photo" role="img" aria-label="Hillside monitoring station with a utility vehicle on green grass under a cloudy sky"></div>
<div class="abs badge"><b>15+</b><small>Years<br>of Experience</small></div>
<h2 class="abs about-title">About Us</h2>
<div class="abs divider" style="left:674px;top:848px"><span></span><i></i><span></span></div>
<p class="abs about-text">Welcome to Brovalux, your reliable partner in delivering innovative solutions. Our team of skilled professionals is committed to excellence, ensuring every project is handled with precision, efficiency,andintegrity.Wesolveproblemsinthefield,buildrobustinfrastructure,anddeliveraccuratedatatoourclients.Letushelpyouachieveyourgoalswithourtailored</p>
<div class="abs btn-dark" style="left:672px;top:1068px;width:140px;height:41px">Get Started
  <svg width="12" height="12" viewBox="0 0 12 12"><path d="M2 10L10 2M4 2h6v6" stroke="#111318" stroke-width="1.6" fill="none"/></svg></div>

<!-- Services -->
<div class="abs services-bg"></div>
<svg class="band" style="top:1260px" width="1200" height="130" viewBox="0 0 1200 130">
  <polygon points="0,0 1200,0 1200,118 826,12 0,106" fill="#ffffff"/>
  <polygon points="0,106 826,12 1200,118 1200,136 826,18 0,130" fill="#4a74f5"/>
</svg>
<h2 class="abs section-title" style="top:1395px">Our Services</h2>
<div class="abs divider" style="left:558px;top:1451px"><span></span><i></i><span></span></div>

<div class="abs card" style="left:141px;top:1511px;width:293px;height:621px">
  <div class="card-img" role="img" aria-label="Red inflatable boat with equipment on the open sea" style="background:linear-gradient(180deg,#8fb4d6 0%,#5c86b0 50%,#b0262b 75%,#2a2a2a 100%)"></div>
  <h3>Fieldwork Solutions</h3>
  <ul><li>Project management &amp; logistics</li><li>Efficient product rollouts</li><li>Equipment Installation &amp; Maintenance</li><li>SurveyingTechniques</li><li>Precision GNSS instrumentation</li><li>Seismic Instrumentation</li><li>IOT Sensors</li><li>Reliable Communications Systems</li><li>Environmental sensors</li></ul>
</div>
<div class="abs card" style="left:454px;top:1511px;width:293px;height:621px">
  <div class="card-img" role="img" aria-label="Hilltop reference station overlooking a coastal bay" style="background:linear-gradient(180deg,#c9cdd2 0%,#9ea7ad 45%,#7d7a55 75%,#5b5a3a 100%)"></div>
  <h3>Positioning And Monitoring</h3>
  <ul><li>Real-Time Kinematic (RTK) Solutions</li><li>Custom GNSS Base stations</li><li>NTRIP service</li><li>Tailored Monitoring Solutions</li><li>Environmental Monitoring</li><li>Robust communication Systems</li><li>Internet of Things (IoT) Integration</li><li>Solar powered systems</li><li>Smart Sensor Networks</li></ul>
</div>
<div class="abs card" style="left:766px;top:1511px;width:293px;height:621px">
  <div class="card-img" role="img" aria-label="Mechanical parts and calipers resting on technical drawings" style="background:linear-gradient(135deg,#e4e4e4 0%,#c9c9c9 50%,#9a9a9a 100%)"></div>
  <h3>Design And Prototyping</h3>
  <ul><li>Mechanical Component Design</li><li>Robust Field Equipment Infrastructure</li><li>Remote Monitoring System Design</li><li>3D modelling</li><li>Standalone Power Solutions</li><li>Wireless Communication Solutions</li><li>Real-Time Data Transmission</li><li>Rapid Prototyping</li><li>Field Deployment and Testing</li></ul>
</div>

<svg class="band" style="top:2200px" width="1200" height="130" viewBox="0 0 1200 130">
  <polygon points="0,10 358,117 1200,10 1200,130 0,130" fill="#ffffff"/>
  <polygon points="0,0 358,117 1200,0 1200,24 358,117 0,26" fill="#4a74f5"/>
</svg>

<!-- Case studies -->
<h2 class="abs section-title" style="top:2406px">Case Studies</h2>
<div class="abs divider" style="left:558px;top:2463px"><span></span><i></i><span></span></div>

<svg class="abs nav-arrow" style="left:68px;top:2637px" viewBox="0 0 30 56"><path d="M26 2L4 28l22 26" stroke="#9bb1f5" stroke-width="3" fill="none"/></svg>
<svg class="abs nav-arrow" style="left:1101px;top:2637px" viewBox="0 0 30 56"><path d="M4 2l22 26L4 54" stroke="#4a74f5" stroke-width="3" fill="none"/></svg>

<div class="abs case-img" style="left:141px;top:2525px;width:442px;height:280px;background:linear-gradient(180deg,#5f8ed2 0%,#a9c3e3 45%,#b9b6ad 65%,#7d7a72 100%)" role="img" aria-label="Solar-powered GNSS station on a rocky mountain ridge"></div>
<div class="abs case-box" style="left:180px;top:2666px;width:363px;height:239px">
  <h4>GNSS Cors Station Upgrade<br>And Survey</h4>
  <p>Upgrade and reference mark survey of GNSSContinuouslyOperatingReferenceStations(CORS)fortheLandGridpositioningnetwork.This project enhanced the accuracy and reliability of the LandGrid positioning network, crucialforawiderangeofapplicationsincludinglandsurveying,construction,andgeospatialresearch.</p>
</div>

<div class="abs case-img" style="left:617px;top:2525px;width:441px;height:280px;background:linear-gradient(180deg,#d7dbde 0%,#b8c0c4 40%,#6e8a5a 65%,#4a6a3c 100%)" role="img" aria-label="Green equipment case in a field beside a satellite dish"></div>
<div class="abs case-box" style="left:655px;top:2666px;width:364px;height:239px">
  <h4>Communications Hub<br>Upgrade</h4>
  <p>Installation of a satellite interface for TerraWatch to ensurereliabledatatransmissionforscientificresearchand monitoringofgeologicalhazards.TerraWatchoperatesacomprehensivenetworkofover1000monitoringinstrumentsacrossNewZealand,providing 24/7 data collection and analysis for earthquakes, volcanic activity, landslides,</p>
</div>

<!-- Contact form -->
<h2 class="abs section-title" style="top:2982px">Get in touch with us!</h2>
<div class="abs divider" style="left:558px;top:3039px"><span></span><i></i><span></span></div>

<div class="abs field active" style="top:3110px;height:53px">Name</div>
<div class="abs float-label">Your Name</div>
<div class="abs field" style="top:3185px;height:53px">Subject</div>
<div class="abs field" style="top:3260px;height:53px">Phone No</div>
<div class="abs field" style="top:3336px;height:53px">Email Address</div>
<div class="abs field area" style="top:3410px;height:100px">Massage</div>
<div class="abs btn-blue" style="left:551px;top:3534px;width:97px;height:41px;font-size:12.5px">Send
  <svg width="14" height="14" viewBox="0 0 14 14"><polygon points="1,1 13,7 1,13 3,7" fill="#fff"/></svg></div>

<!-- Footer -->
<div class="abs footer-bg"></div>
<svg class="band" style="top:3640px" width="1200" height="140" viewBox="0 0 1200 140">
  <polygon points="0,0 1200,0 1200,118 843,32 0,116" fill="#ffffff"/>
  <polygon points="0,116 843,32 1200,118 1200,140 0,140" fill="#0f1730"/>
  <polygon points="0,116 843,32 0,136" fill="#4a74f5"/>
</svg>
<div class="abs brand" style="left:143px;top:3880px"><span class="brand-dot"></span>Brovalux</div>

<div class="abs foot-h" style="left:378px;top:3807px">RESOURCES</div>
<div class="abs" style="left:378px;top:3843px">
  <div class="foot-link">Privacy Policy</div><div class="foot-link">Terms of Service</div><div class="foot-link">Contact</div>
</div>

<div class="abs foot-h" style="left:570px;top:3807px">CONTACT DETAILS</div>
<div class="abs" style="left:570px;top:3846px;width:240px">
  <div class="foot-link" style="display:flex;gap:8px;align-items:center"><svg width="12" height="14" viewBox="0 0 12 14"><path d="M6 13S1 8 1 5a5 5 0 0110 0c0 3-5 8-5 8z" fill="#fff"/><circle cx="6" cy="5" r="1.8" fill="#0c1330"/></svg>Lorem Ipsum is simply dummy text</div>
  <div class="foot-link" style="display:flex;gap:8px;align-items:flex-start;margin-top:12px;line-height:19px"><svg width="12" height="12" viewBox="0 0 12 12" style="margin-top:3px"><path d="M2 1l2.5 0 1 3-1.5 1a7 7 0 003 3l1-1.5 3 1V10a1 1 0 01-1 1A10 10 0 011 2a1 1 0 011-1z" fill="#fff"/></svg><span>Phone<br>+64 21 555 0192</span></div>
  <div class="foot-link" style="display:flex;gap:8px;align-items:flex-start;margin-top:10px;line-height:19px"><svg width="13" height="10" viewBox="0 0 13 10" style="margin-top:4px"><rect x=".5" y=".5" width="12" height="9" fill="#fff"/><path d="M.5.5l6 5 6-5" stroke="#0c1330" fill="none"/></svg><span>Email<br>hi@brovalux.nz</span></div>
</div>

<div class="abs foot-h" style="left:826px;top:3807px">NEWSLETTER</div>
<div class="abs newsletter">Enter your email
  <div class="nl-btn"><svg width="14" height="14" viewBox="0 0 14 14"><polygon points="1,1 13,7 1,13 3,7" fill="#fff"/></svg></div>
</div>

<div class="abs copyright">Copyright © Brovalux 2024. All Rights Reserved.</div>

</body>
</html>
```